Criação de Layout Web-Design para Contabilidade & Finanças
A empresa queria:
" A Orvalis é um HUB financeiro para o cliente. Através da Orvalis, o cliente tem acesso a serviços de Investimentos (Orvalis Investimentos), Crédito (Orvalis Crédito), Seguros (Orvalis Seguros), Câmbio, Consultoria Financeira, Tributária, Patrimonial, Jurídica etc. Funciona como um "family office" voltado a atender com excelência e assertividade as demandas de um cliente de alto patrimônio. Isso é possível graças a uma extensa e qualificada rede de parceiros. A Orvalis foca em investimentos e os parceiros focam nas outras demandas. "

```html
<!DOCTYPE html>
<html lang="pt-BR">
<head>
<meta charset="UTF-8">
<title>Orvalis — Hub Financeiro</title>
<link rel="stylesheet" href="https://fonts.googleapis.com/css2?family=Cinzel:wght@400;600&family=Montserrat:wght@400;600;700&display=swap">
<style>
  :root{
    --page-bg:#1b1c1e;
    --hero-deep:#050506;
    --hero-mid:#1d1e22;
    --hero-light:#5a5c61;
    --map-tone:#2a2c31;
    --text-main:#f2f2f2;
    --text-soft:#c9c9c9;
    --accent-gold:#c9a45c;
  }
  *{margin:0;padding:0;box-sizing:border-box}
  html,body{width:1200px;height:1200px;overflow:hidden}
  body{background:var(--page-bg);display:flex;align-items:center;justify-content:center;font-family:"Montserrat",sans-serif}
  .site{position:relative;width:1200px;height:750px;overflow:hidden;background:var(--hero-deep)}
  .hero-visual{position:absolute;inset:0;
    background:
      radial-gradient(ellipse 30% 38% at 52% 42%, rgba(200,170,150,.35), transparent 70%),
      radial-gradient(ellipse 55% 60% at 40% 30%, var(--hero-light), transparent 75%),
      linear-gradient(180deg, var(--hero-mid) 0%, var(--hero-deep) 70%)}
  .hero-map{position:absolute;left:0;right:0;bottom:0;height:230px;
    background:radial-gradient(ellipse 60% 70% at 50% 100%, var(--map-tone), transparent 80%)}
  .hero-shade{position:absolute;inset:0;background:linear-gradient(180deg,rgba(0,0,0,.55) 0%,rgba(0,0,0,.15) 35%,rgba(0,0,0,.45) 100%)}
  .site-header{position:absolute;top:0;left:0;right:0;display:flex;align-items:center;justify-content:space-between;padding:46px 90px 0 130px}
  .brand{display:flex;align-items:center;gap:12px;color:var(--text-main);font-family:"Montserrat",sans-serif;font-weight:700;font-size:34px;letter-spacing:2px}
  .brand-dot{width:16px;height:16px;border-radius:50%;background:var(--accent-gold)}
  .main-nav{display:flex;gap:26px}
  .main-nav a{font-family:"Cinzel",serif;font-size:19px;color:var(--text-main);text-decoration:none;letter-spacing:1px;padding-bottom:4px}
  .main-nav a.is-active{border-bottom:2px solid var(--text-main)}
  .hero-content{position:absolute;left:0;right:0;top:305px;text-align:center;color:var(--text-main)}
  .hero-title{font-family:"Cinzel",serif;font-weight:400;font-size:31px;line-height:1.22;letter-spacing:2px;text-shadow:0 2px 8px rgba(0,0,0,.7)}
  .hero-services{margin-top:16px;font-size:14px;font-weight:600;color:var(--text-soft)}
  .cta{display:inline-block;margin-top:18px;padding:6px 22px;border:2px solid var(--text-main);border-radius:14px;font-family:"Cinzel",serif;font-size:19px;letter-spacing:2px;color:var(--text-main);text-decoration:none;background:rgba(0,0,0,.35)}
</style>
</head>
<body>
  <main class="site">
    <div class="hero-visual" role="img" aria-label="Fotografia de executivo de terno tocando uma tela digital, com um mapa-múndi conectado por linhas de rede na parte inferior"></div>
    <div class="hero-map"></div>
    <div class="hero-shade"></div>

    <header class="site-header">
      <div class="brand"><span class="brand-dot"></span>ORVALIS</div>
      <nav class="main-nav">
        <a href="#" class="is-active">Home</a>
        <a href="#">Quem Somos</a>
        <a href="#">Serviços</a>
        <a href="#">Portfolio</a>
        <a href="#">Contato</a>
      </nav>
    </header>

    <section class="hero-content">
      <h1 class="hero-title">Inteligência em Investimentos e Serviços<br>Financeiros para clientes de alto patrimônio</h1>
      <p class="hero-services">Investimentos (Orvalis Investimentos), Crédito (Orvalis Crédito), Seguros (Orvalis Seguros)</p>
      <a href="#" class="cta">Saiba Mais</a>
    </section>
  </main>
</body>
</html>
```